New web page, 2 companies on the one page

A new web page for an engineering consultancy and maintenance management company

Carlow & Associates is the parent company covering the design and consultancy
Viltrop Engineering is the Maintenance and Reliability company

Target Market(s)

Food & Beverage, ingredients Manufacturing
engineering managers

Coding

Coded - Design and coding required

Number of Pages Required

1 page

Font styles to use
Other font styles liked:
• Roboto

Colors
1861ab
85acd3
d0dfed
cee9f5

```html
<!DOCTYPE html>
<html lang="en">
<head>
<meta charset="utf-8">
<title>Carlow &amp; Associates – Home Page Variants</title>
<link href="https://fonts.googleapis.com/css2?family=Montserrat:wght@400;500;600;700;800;900&display=swap" rel="stylesheet">
<style>
:root{
  --backdrop:#e4e4e6;
  --blue:#6d98cd;
  --blue-deep:#1861ab;
  --blue-soft:#85acd3;
  --sky:#c3e1f2;
  --mist:#f3f0f3;
  --ink:#222226;
  --text:#4a4a50;
  --line-gray:#5d5d62;
  --night:#1d1b1c;
  --white:#ffffff;
}
*{box-sizing:border-box;margin:0;padding:0}
html,body{width:710px;height:1200px;overflow:hidden;background:var(--backdrop)}
body{font-family:"Montserrat",Arial,sans-serif;color:var(--ink)}
.icon-defs{position:absolute;width:0;height:0}
.stage{position:absolute;left:0;top:0;width:1484px;height:2507px;transform:scale(0.4784);transform-origin:0 0}
.page{position:absolute;top:62px;width:649px;height:2396px;background:var(--white);overflow:hidden}
.page--a{left:60px}
.page--b{left:769px}
.abs{position:absolute}

/* header */
.brand{position:absolute;left:71px;top:14px;display:flex;align-items:center;gap:7px}
.brand-mark{width:30px;height:30px;background:var(--line-gray)}
.brand-name{font-weight:800;font-size:12px;letter-spacing:.3px;color:var(--ink);text-transform:uppercase;line-height:1}
.contact-chip{position:absolute;top:13px;display:flex;gap:6px;align-items:center}
.chip-dot{width:14px;height:14px;border-radius:50%;background:var(--blue);display:flex;align-items:center;justify-content:center}
.chip-dot svg{width:8px;height:8px}
.chip-label{font-size:5.5px;font-weight:500;color:var(--text);letter-spacing:.3px}
.chip-value{font-size:8.5px;font-weight:600;color:var(--ink)}
.nav{position:absolute;top:41px;left:247px;display:flex;gap:0}
.nav a{font-size:7.5px;font-weight:600;color:var(--ink);text-decoration:none;margin-right:24px}
.nav a.is-current{color:var(--blue);text-decoration:underline}

/* hero */
.hero{position:absolute;left:0;top:58px;width:649px;height:296px;clip-path:polygon(0 0,100% 0,100% 253px,50% 295px,0 258px)}
.hero--city{background:radial-gradient(ellipse at 62% 40%,#6d8fbf 0%,transparent 55%),linear-gradient(180deg,#253c63 0%,#4b6c9b 38%,#2a4670 65%,#17284a 100%)}
.hero--team{background:radial-gradient(ellipse at 65% 45%,#7f93b5 0%,transparent 50%),linear-gradient(180deg,#dfe3ea 0%,#b3bfd1 45%,#8496b3 100%)}
.hero-title{position:absolute;color:var(--white);font-weight:900;font-size:21px;line-height:26px;letter-spacing:.4px}
.hero-btn{position:absolute;height:22px;width:68px;border:1.5px solid var(--white);color:var(--white);font-size:7px;font-weight:600;display:flex;align-items:center;justify-content:center}
.hero-btn--fill{background:var(--blue)}
.dots{position:absolute;top:326px;left:300px;display:flex;gap:5px}
.dots span{width:4px;height:4px;border-radius:50%;background:#dfe6f0}
.dots span.on{background:var(--blue);box-shadow:0 0 0 1.5px #fff}

/* sections */
.band-mist{position:absolute;left:0;width:649px;background:var(--mist)}
.section-title{position:absolute;left:0;width:649px;text-align:center;font-weight:800;font-size:11.5px;letter-spacing:.2px;color:var(--ink)}
.section-title::after{content:"";display:block;width:22px;height:2px;background:var(--blue);margin:7px auto 0}
.section-title--left{text-align:left;left:71px;width:auto}
.section-title--left::after{margin:7px 0 0}
.rule{position:absolute;pointer-events:none}

/* services */
.service{position:absolute;width:180px;text-align:center}
.service-disc{width:52px;height:52px;border-radius:50%;background:var(--blue);margin:0 auto;display:flex;align-items:center;justify-content:center;box-shadow:0 0 0 2px #e4e9f2}
.service-disc svg{width:28px;height:28px}
.service-name{margin-top:9px;font-size:8px;font-weight:600;line-height:10.5px;color:var(--ink)}
.col-divider{position:absolute;width:1px;background:#d9d5dc}

/* welcome */
.welcome-photo{position:absolute;left:71px;top:791px;width:249px;height:248px;clip-path:polygon(0 0,50% 12%,100% 0,100% 100%,50% 89%,0 100%);background:linear-gradient(120deg,#4e4a48 0%,#8a7a6c 40%,#c98a4a 60%,#5a5f6a 100%)}
.eyebrow{font-size:9px;font-weight:500;color:var(--ink)}
.welcome-title{font-size:14.5px;font-weight:800;color:var(--ink);letter-spacing:.2px}
.copy{font-size:8.6px;line-height:13px;color:var(--text)}
.btn{position:absolute;background:var(--blue);color:var(--white);font-size:6px;font-weight:700;display:flex;align-items:center;justify-content:center;letter-spacing:.2px}

/* why */
.why-item{position:absolute;left:71px;width:230px;display:flex;gap:12px}
.why-item svg{flex:none;width:28px;height:28px}
.why-head{font-size:8px;font-weight:600;color:var(--ink);margin-bottom:4px}
.why-copy{font-size:7.2px;line-height:10.5px;color:var(--text)}
.why-sep{position:absolute;left:71px;width:230px;height:1px;background:#dcd8de}
.why-photo{position:absolute;left:328px;top:1078px;width:321px;height:293px;clip-path:polygon(0 0,100% 0,100% 250px,0 293px);background:linear-gradient(160deg,#9fb4d6 0%,#55698f 35%,#2d3c5e 55%,#d4a39a 80%,#f0c7a6 100%)}

/* stats */
.stats{position:absolute;left:0;top:1328px;width:649px;height:244px;background:linear-gradient(180deg,#2a3550 0%,#1f2433 45%,#2b2024 100%)}
.stat{position:absolute;width:150px;text-align:center;color:var(--white)}
.stat svg{width:22px;height:22px;display:block;margin:0 auto 10px}
.stat-num{font-size:20px;font-weight:800;line-height:1}
.stat-label{font-size:6.8px;font-weight:500;letter-spacing:.3px;margin-top:6px}
.stat-divider{position:absolute;width:1px;background:rgba(255,255,255,.35)}

/* blog */
.blog-band{position:absolute;left:0;top:1572px;width:649px;height:195px;background:var(--sky)}
.post{position:absolute;top:1640px;width:160px;height:242px;background:var(--white);box-shadow:0 2px 6px rgba(0,0,0,.12)}
.post-photo{height:126px}
.post-photo--site{background:linear-gradient(160deg,#aab7c7 0%,#6f7d8f 50%,#3e4a5e 100%)}
.post-photo--plans{background:linear-gradient(160deg,#5a6478 0%,#c8ccd2 55%,#2d2f36 100%)}
.post-photo--data{background:linear-gradient(160deg,#2f4460 0%,#6b87aa 50%,#1e2a3d 100%)}
.post-body{padding:13px 15px 0}
.post-title{font-size:8px;font-weight:600;line-height:10.5px;color:var(--ink)}
.post-copy{font-size:7px;line-height:10px;color:var(--text);margin-top:7px}
.post .btn{position:relative;width:50px;height:15px;margin-top:9px}

/* feature */
.feature-photo{position:absolute;left:71px;top:1943px;width:289px;height:206px;background:linear-gradient(150deg,#3b3a3a 0%,#8c8a86 45%,#d2cbc0 60%,#4a4844 100%)}
.feature-title{font-size:11.5px;font-weight:800;line-height:15.5px;color:var(--ink)}

/* footer */
.footer{position:absolute;left:0;top:2164px;width:649px;height:232px;background:var(--night);clip-path:polygon(0 0,50% 42px,100% 0,100% 100%,0 100%)}
.foot-brand{position:absolute;left:71px;top:2254px;display:flex;align-items:center;gap:8px}
.foot-brand .brand-mark{width:40px;height:40px;background:var(--blue)}
.foot-brand .brand-name{color:var(--white);font-size:13px;line-height:15px}
.foot-head{position:absolute;top:2237px;font-size:6.5px;font-weight:700;color:var(--white);letter-spacing:.3px}
.foot-menu{position:absolute;left:270px;top:2257px;list-style:none}
.foot-menu li{font-size:6px;color:#d6d6d8;line-height:10.6px}
.foot-row{position:absolute;display:flex;gap:6px;align-items:flex-start}
.foot-disc{width:11px;height:11px;border-radius:50%;background:var(--white);flex:none;display:flex;align-items:center;justify-content:center}
.foot-disc svg{width:6px;height:6px}
.foot-text{font-size:5.8px;line-height:7.5px;color:#d6d6d8}
.foot-line{position:absolute;left:71px;top:2352px;width:507px;height:1px;background:#3b393a}
.copyright{position:absolute;left:0;width:649px;top:2377px;text-align:center;font-size:5.5px;color:#bdbdc0}
</style>
</head>
<body>
<svg class="icon-defs" aria-hidden="true">
  <defs>
    <symbol id="i-gear" viewBox="0 0 24 24"><circle cx="12" cy="12" r="4" fill="none" stroke="#fff" stroke-width="2"/><path d="M12 2v4M12 18v4M2 12h4M18 12h4M4.9 4.9l2.8 2.8M16.3 16.3l2.8 2.8M4.9 19.1l2.8-2.8M16.3 7.7l2.8-2.8" stroke="#fff" stroke-width="2.4" stroke-linecap="round"/></symbol>
    <symbol id="i-gauge" viewBox="0 0 24 24"><path d="M4 17a8 8 0 1 1 16 0" fill="none" stroke="#fff" stroke-width="2"/><path d="M12 17l4-6" stroke="#fff" stroke-width="2" stroke-linecap="round"/></symbol>
    <symbol id="i-flow" viewBox="0 0 24 24"><rect x="3" y="3" width="7" height="5" fill="none" stroke="#fff" stroke-width="1.8"/><rect x="14" y="3" width="7" height="5" fill="none" stroke="#fff" stroke-width="1.8"/><rect x="3" y="16" width="7" height="5" fill="none" stroke="#fff" stroke-width="1.8"/><rect x="14" y="16" width="7" height="5" fill="none" stroke="#fff" stroke-width="1.8"/><path d="M10 5.5h4M17.5 8v8M6.5 8v8" stroke="#fff" stroke-width="1.8"/></symbol>
    <symbol id="i-bulb" viewBox="0 0 24 24"><path d="M12 3a6 6 0 0 0-3.5 10.9V17h7v-3.1A6 6 0 0 0 12 3z" fill="none" stroke="#fff" stroke-width="1.8"/><path d="M9.5 20h5" stroke="#fff" stroke-width="1.8"/></symbol>
    <symbol id="i-clip" viewBox="0 0 24 24"><rect x="5" y="4" width="12" height="16" rx="1" fill="none" stroke="#fff" stroke-width="1.8"/><path d="M8 9h6M8 12h6M8 15h3" stroke="#fff" stroke-width="1.6"/><circle cx="17" cy="17" r="3.5" fill="#6d98cd" stroke="#fff" stroke-width="1.6"/></symbol>
    <symbol id="i-tree" viewBox="0 0 24 24"><rect x="9" y="3" width="6" height="5" fill="none" stroke="#fff" stroke-width="1.8"/><rect x="3" y="16" width="6" height="5" fill="none" stroke="#fff" stroke-width="1.8"/><rect x="15" y="16" width="6" height="5" fill="none" stroke="#fff" stroke-width="1.8"/><path d="M12 8v4M6 16v-4h12v4" fill="none" stroke="#fff" stroke-width="1.8"/></symbol>
    <symbol id="i-list" viewBox="0 0 24 24"><rect x="5" y="3" width="12" height="18" rx="1" fill="none" stroke="#fff" stroke-width="1.8"/><path d="M8 8h6M8 11h6M8 14h6M8 17h4" stroke="#fff" stroke-width="1.6"/></symbol>
    <symbol id="i-hands" viewBox="0 0 24 24"><path d="M3 9l9-5 9 5" fill="none" stroke="#fff" stroke-width="1.8"/><path d="M5 10v7M9 10v7M15 10v7M19 10v7M3 19h18" stroke="#fff" stroke-width="1.8"/></symbol>
    <symbol id="i-headset" viewBox="0 0 24 24"><path d="M4 14v-2a8 8 0 0 1 16 0v2" fill="none" stroke="#6d98cd" stroke-width="1.6"/><rect x="3" y="13" width="4" height="6" rx="1.5" fill="none" stroke="#6d98cd" stroke-width="1.6"/><rect x="17" y="13" width="4" height="6" rx="1.5" fill="none" stroke="#6d98cd" stroke-width="1.6"/></symbol>
    <symbol id="i-timer" viewBox="0 0 24 24"><path d="M3 5h18M3 9h6M3 13h5M3 17h6" stroke="#6d98cd" stroke-width="1.6"/><circle cx="15" cy="14" r="5" fill="none" stroke="#6d98cd" stroke-width="1.6"/><path d="M15 11.5V14h2" stroke="#6d98cd" stroke-width="1.6" fill="none"/></symbol>
    <symbol id="i-sun" viewBox="0 0 24 24"><circle cx="12" cy="12" r="5" fill="none" stroke="#6d98cd" stroke-width="1.6"/><circle cx="12" cy="12" r="2" fill="none" stroke="#6d98cd" stroke-width="1.6"/><path d="M12 2v3M12 19v3M2 12h3M19 12h3M5 5l2 2M17 17l2 2M5 19l2-2M17 7l2-2" stroke="#6d98cd" stroke-width="1.6"/></symbol>
    <symbol id="i-case" viewBox="0 0 24 24"><rect x="2" y="7" width="20" height="13" rx="2" fill="#fff"/><path d="M8 7V5h8v2" fill="none" stroke="#fff" stroke-width="2"/><path d="M2 13h20" stroke="#2a3550" stroke-width="1.5"/></symbol>
    <symbol id="i-board" viewBox="0 0 24 24"><rect x="3" y="3" width="18" height="18" fill="none" stroke="#fff" stroke-width="2"/><path d="M3 8h18M12 8v13M3 14h18" stroke="#fff" stroke-width="2"/></symbol>
    <symbol id="i-team" viewBox="0 0 24 24"><circle cx="6" cy="6" r="2.5" fill="#fff"/><circle cx="12" cy="5" r="2.5" fill="#fff"/><circle cx="18" cy="6" r="2.5" fill="#fff"/><rect x="4" y="10" width="4" height="10" rx="1.5" fill="#fff"/><rect x="10" y="9" width="4" height="12" rx="1.5" fill="#fff"/><rect x="16" y="10" width="4" height="10" rx="1.5" fill="#fff"/></symbol>
    <symbol id="i-thumb" viewBox="0 0 24 24"><rect x="2" y="10" width="5" height="11" fill="#fff"/><path d="M9 10l4-8c2 0 2.5 1.5 2 4l-.5 3H21l-1.5 12H9z" fill="#fff"/></symbol>
    <symbol id="i-mail" viewBox="0 0 24 24"><rect x="3" y="6" width="18" height="12" fill="none" stroke="#fff" stroke-width="2.5"/><path d="M3 6l9 7 9-7" fill="none" stroke="#fff" stroke-width="2.5"/></symbol>
    <symbol id="i-phone" viewBox="0 0 24 24"><path d="M6 3l4 4-2 3a12 12 0 0 0 6 6l3-2 4 4-3 3C10 21 3 14 3 6z" fill="#fff"/></symbol>
    <symbol id="i-pin" viewBox="0 0 24 24"><path d="M12 2a7 7 0 0 0-7 7c0 5 7 13 7 13s7-8 7-13a7 7 0 0 0-7-7z" fill="#1d1b1c"/><circle cx="12" cy="9" r="2.5" fill="#fff"/></symbol>
    <symbol id="i-phone-dark" viewBox="0 0 24 24"><path d="M6 3l4 4-2 3a12 12 0 0 0 6 6l3-2 4 4-3 3C10 21 3 14 3 6z" fill="#1d1b1c"/></symbol>
    <symbol id="i-mail-dark" viewBox="0 0 24 24"><rect x="3" y="6" width="18" height="12" fill="none" stroke="#1d1b1c" stroke-width="3"/><path d="M3 6l9 7 9-7" fill="none" stroke="#1d1b1c" stroke-width="3"/></symbol>
  </defs>
</svg>

<main class="stage">

<!-- ============ VARIANT A ============ -->
<section class="page page--a" aria-label="Home page, variant A">
  <header>
    <div class="brand"><span class="brand-mark"></span><span class="brand-name">Carlow &amp; Associates</span></div>
    <div class="contact-chip" style="left:339px"><span class="chip-dot"><svg><use href="#i-mail"/></svg></span><div><div class="chip-label">EMAIL US</div><div class="chip-value">info@carlowassoc.com</div></div></div>
    <div class="contact-chip" style="left:491px"><span class="chip-dot"><svg><use href="#i-phone"/></svg></span><div><div class="chip-label">CALL US</div><div class="chip-value">888.888.8888</div></div></div>
    <nav class="nav"><a class="is-current">HOME</a><a>ABOUT US</a><a>SERVICES</a><a>PROJECTS</a><a>NEWS</a><a>CONTACT US</a></nav>
  </header>

  <div class="band-mist" style="top:296px;height:460px;clip-path:polygon(0 0,100% 0,100% 417px,50% 457px,0 417px)"></div>
  <div class="hero hero--city" role="img" aria-label="Businessman overlooking a night city skyline with network lines"></div>
  <h1 class="hero-title" style="left:404px;top:88px">ENGINEERING<br>CONSULTANCY</h1>
  <div class="hero-btn" style="left:406px;top:147px">READ MORE</div>
  <div class="dots"><span></span><span></span><span class="on"></span><span></span><span></span></div>
  <svg class="rule" style="left:0;top:0" width="649" height="2396"><path d="M0 316L325 353" stroke="#5d5d62" stroke-width="4"/><path d="M325 353L649 311" stroke="#6d98cd" stroke-width="4"/><path d="M0 713L325 753" stroke="#5d5d62" stroke-width="4"/><path d="M325 753L649 713" stroke="#6d98cd" stroke-width="4"/></svg>

  <h2 class="section-title" style="top:380px">OUR SERVICES</h2>
  <div class="col-divider" style="left:234px;top:430px;height:275px"></div>
  <div class="col-divider" style="left:421px;top:430px;height:275px"></div>
  <div class="service" style="left:43px;top:424px"><div class="service-disc"><svg><use href="#i-gear"/></svg></div><p class="service-name">Major Equipment and Services<br>Installation &amp; Commissioning</p></div>
  <div class="service" style="left:235px;top:424px"><div class="service-disc"><svg><use href="#i-gear"/></svg></div><p class="service-name">Engineering &amp; Maintenance<br>Management</p></div>
  <div class="service" style="left:428px;top:424px"><div class="service-disc"><svg><use href="#i-gauge"/></svg></div><p class="service-name">Manufacturing Performance<br>Measurement</p></div>
  <div class="service" style="left:43px;top:529px"><div class="service-disc"><svg><use href="#i-flow"/></svg></div><p class="service-name">Process &amp; Facilities Design</p></div>
  <div class="service" style="left:235px;top:529px"><div class="service-disc"><svg><use href="#i-bulb"/></svg></div><p class="service-name">Project Management</p></div>
  <div class="service" style="left:428px;top:529px"><div class="service-disc"><svg><use href="#i-clip"/></svg></div><p class="service-name">Maintenance Execution</p></div>
  <div class="service" style="left:43px;top:626px"><div class="service-disc"><svg><use href="#i-tree"/></svg></div><p class="service-name">SCADA</p></div>
  <div class="service" style="left:235px;top:626px"><div class="service-disc"><svg><use href="#i-list"/></svg></div><p class="service-name">Vision Inspection Systems</p></div>
  <div class="service" style="left:428px;top:626px"><div class="service-disc"><svg><use href="#i-hands"/></svg></div><p class="service-name">Acquisition Due Diligence</p></div>

  <div class="welcome-photo" role="img" aria-label="Engineer in hard hat and safety vest using a tablet"></div>
  <p class="eyebrow abs" style="left:345px;top:790px">WELCOME TO</p>
  <h2 class="welcome-title abs" style="left:345px;top:803px">CARLOW &amp; ASSOCIATES</h2>
  <div class="abs" style="left:345px;top:845px;width:230px">
    <p class="copy">Carlow &amp; Associates is specialised manufacturing engineering support organisation that can provide fast, nimble, and flexible services.</p>
    <p class="copy" style="margin-top:13px">We have a proven track record in delivering tangible outcomes in process design and fit-out, project management, manufacturing process and maintenance design and execution.</p>
    <p class="copy" style="margin-top:13px">Our specialist focus in food manufacturing across a range of sectors allows our team to deliver real benefits to performance and recognition of the clients investment</p>
  </div>
  <div class="btn" style="left:345px;top:1024px;width:53px;height:16px">READ MORE</div>

  <div class="stats"></div>
  <div class="band-mist" style="top:1078px;height:293px;clip-path:polygon(0 0,100% 0,100% 250px,328px 293px,0 250px)"></div>
  <div class="why-photo" role="img" aria-label="Engineer in hard hat with city and crane at sunset"></div>
  <svg class="rule" style="left:0;top:1320px" width="649" height="60"><path d="M0 8L328 51" stroke="#5d5d62" stroke-width="4"/><path d="M328 51L649 8" stroke="#6d98cd" stroke-width="4"/></svg>
  <h2 class="section-title section-title--left" style="top:1104px">WHY CHOOSE US</h2>
  <div class="why-item" style="top:1145px"><svg><use href="#i-headset"/></svg><div><p class="why-head">Support</p><p class="why-copy">There are many variations of passages of Lorem Ipsum available, but the majority have.</p></div></div>
  <div class="why-sep" style="top:1197px"></div>
  <div class="why-item" style="top:1210px"><svg><use href="#i-timer"/></svg><div><p class="why-head">Track Record</p><p class="why-copy">There are many variations of passages of Lorem Ipsum available, but the majority have.</p></div></div>
  <div class="why-sep" style="top:1261px"></div>
  <div class="why-item" style="top:1274px"><svg><use href="#i-sun"/></svg><div><p class="why-head">Flexible</p><p class="why-copy">There are many variations of passages of Lorem Ipsum available, but the majority have.</p></div></div>

  <div class="stat-divider" style="left:177px;top:1430px;height:105px"></div>
  <div class="stat-divider" style="left:310px;top:1430px;height:105px"></div>
  <div class="stat" style="left:38px;top:1453px"><svg><use href="#i-case"/></svg><p class="stat-num">10+</p><p class="stat-label">YEARS OF OPERATION</p></div>
  <div class="stat" style="left:167px;top:1453px"><svg><use href="#i-board"/></svg><p class="stat-num">400</p><p class="stat-label">SUCCESSFUL PROJECTS</p></div>
  <div class="stat" style="left:314px;top:1453px"><svg><use href="#i-team"/></svg><p class="stat-num">150</p><p class="stat-label">QUALIFIED PROFESSIONALS</p></div>
  <div class="stat" style="left:458px;top:1453px"><svg><use href="#i-thumb"/></svg><p class="stat-num">6579</p><p class="stat-label">SATISFIED CUSTOMERS</p></div>

  <div class="blog-band"></div>
  <h2 class="section-title" style="top:1593px">LATEST BLOG</h2>
  <article class="post" style="left:71px"><div class="post-photo post-photo--site" role="img" aria-label="Engineers reviewing a construction site"></div><div class="post-body"><h3 class="post-title">Lorem Ipsum is simply dummy text of the printing</h3><p class="post-copy">There are many variations of passages of Lorem Ipsum avail able, but the majority have.</p><div class="btn">READ MORE</div></div></article>
  <article class="post" style="left:245px"><div class="post-photo post-photo--plans" role="img" aria-label="Engineers with plans in a warehouse"></div><div class="post-body"><h3 class="post-title">Lorem Ipsum is simply dummy text of the printing</h3><p class="post-copy">There are many variations of passages of Lorem Ipsum avail able, but the majority have.</p><div class="btn">READ MORE</div></div></article>
  <article class="post" style="left:418px"><div class="post-photo post-photo--data" role="img" aria-label="Tablet showing data charts on a desk"></div><div class="post-body"><h3 class="post-title">Lorem Ipsum is simply dummy text of the printing</h3><p class="post-copy">There are many variations of passages of Lorem Ipsum avail able, but the majority have.</p><div class="btn">READ MORE</div></div></article>

  <div class="band-mist" style="top:1915px;height:260px"></div>
  <div class="feature-photo" role="img" aria-label="Team meeting around a table seen from above"></div>
  <h2 class="feature-title abs" style="left:385px;top:1963px;width:200px">THERE ARE MANY VARIATIONS OF PASSAGES OF LOREM IPSUM AVAILABLE</h2>
  <p class="copy abs" style="left:385px;top:2022px;width:195px;line-height:12.5px">Sed ut perspiciatis unde omnis iste natus error sit voluptatem accusantium doloremque laud antium, totam rem aperiam, eaque ipsa quae ab illo inventore veritatis et quasi architecto beatae vitae dicta sunt explicabo.</p>
  <div class="btn" style="left:386px;top:2101px;width:64px;height:20px">CONTACT US</div>

  <div class="footer"></div>
  <svg class="rule" style="left:0;top:2160px" width="649" height="50"><path d="M0 4L325 46" stroke="#5d5d62" stroke-width="4"/><path d="M325 46L649 4" stroke="#6d98cd" stroke-width="4"/></svg>
  <div class="foot-brand"><span class="brand-mark"></span><span class="brand-name">VILTROP<br>ENGINEERING</span></div>
  <p class="foot-head" style="left:270px">MENU</p>
  <ul class="foot-menu"><li>HOME</li><li>ABOUT US</li><li>SERVICES</li><li>PROJECTS</li><li>NEWS</li><li>CONTACT US</li></ul>
  <p class="foot-head" style="left:374px">CONTACT US</p>
  <div class="foot-row" style="left:374px;top:2258px"><span class="foot-disc"><svg><use href="#i-pin"/></svg></span><p class="foot-text">2210 Harbor Lane<br>Corvale, CA 90410</p></div>
  <div class="foot-row" style="left:374px;top:2285px"><span class="foot-disc"><svg><use href="#i-phone-dark"/></svg></span><p class="foot-text">Call Us<br>888.888.8888</p></div>
  <div class="foot-row" style="left:374px;top:2312px"><span class="foot-disc"><svg><use href="#i-mail-dark"/></svg></span><p class="foot-text">E mail Us<br>info@CarlowAssoc.com</p></div>
  <p class="foot-head" style="left:518px">FOLLOW US</p>
  <div class="foot-row" style="left:518px;top:2258px"><span class="foot-disc"></span><p class="foot-text">Like us on<br>SOCIAL PAGE</p></div>
  <div class="foot-row" style="left:518px;top:2285px"><span class="foot-disc"></span><p class="foot-text">Follow us on<br>NEWS FEED</p></div>
  <div class="foot-row" style="left:518px;top:2312px"><span class="foot-disc"></span><p class="foot-text">Follow us on<br>PRO NETWORK</p></div>
  <div class="foot-line"></div>
  <p class="copyright">Copyright © 2021 All Rights Reserved</p>
</section>

<!-- ============ VARIANT B ============ -->
<section class="page page--b" aria-label="Home page, variant B">
  <header>
    <div class="brand"><span class="brand-mark"></span><span class="brand-name">Carlow &amp; Associates</span></div>
    <div class="contact-chip" style="left:339px"><span class="chip-dot"><svg><use href="#i-mail"/></svg></span><div><div class="chip-label">EMAIL US</div><div class="chip-value">info@carlowassoc.com</div></div></div>
    <div class="contact-chip" style="left:491px"><span class="chip-dot"><svg><use href="#i-phone"/></svg></span><div><div class="chip-label">CALL US</div><div class="chip-value">888.888.8888</div></div></div>
    <nav class="nav"><a class="is-current">HOME</a><a>ABOUT US</a><a>SERVICES</a><a>PROJECTS</a><a>NEWS</a><a>CONTACT US</a></nav>
  </header>

  <div class="band-mist" style="top:296px;height:460px;clip-path:polygon(0 0,100% 0,100% 417px,50% 457px,0 417px)"></div>
  <div class="hero hero--team" role="img" aria-label="Engineering team reviewing drawings around a table"></div>
  <h1 class="hero-title" style="left:70px;top:156px">ENGINEERING<br>CONSULTANCY</h1>
  <div class="hero-btn hero-btn--fill" style="left:72px;top:221px">READ MORE</div>
  <div class="dots"><span></span><span></span><span class="on"></span><span></span><span></span></div>
  <svg class="rule" style="left:0;top:0" width="649" height="2396"><path d="M0 316L325 353" stroke="#5d5d62" stroke-width="4"/><path d="M325 353L649 311" stroke="#6d98cd" stroke-width="4"/><path d="M0 713L325 753" stroke="#5d5d62" stroke-width="4"/><path d="M325 753L649 713" stroke="#6d98cd" stroke-width="4"/></svg>

  <h2 class="section-title" style="top:380px">OUR SERVICES</h2>
  <div class="col-divider" style="left:234px;top:430px;height:275px"></div>
  <div class="col-divider" style="left:421px;top:430px;height:275px"></div>
  <div class="service" style="left:43px;top:424px"><div class="service-disc"><svg><use href="#i-gear"/></svg></div><p class="service-name">Major Equipment and Services<br>Installation &amp; Commissioning</p></div>
  <div class="service" style="left:235px;top:424px"><div class="service-disc"><svg><use href="#i-gear"/></svg></div><p class="service-name">Engineering &amp; Maintenance<br>Management</p></div>
  <div class="service" style="left:428px;top:424px"><div class="service-disc"><svg><use href="#i-gauge"/></svg></div><p class="service-name">Manufacturing Performance<br>Measurement</p></div>
  <div class="service" style="left:43px;top:529px"><div class="service-disc"><svg><use href="#i-flow"/></svg></div><p class="service-name">Process &amp; Facilities Design</p></div>
  <div class="service" style="left:235px;top:529px"><div class="service-disc"><svg><use href="#i-bulb"/></svg></div><p class="service-name">Project Management</p></div>
  <div class="service" style="left:428px;top:529px"><div class="service-disc"><svg><use href="#i-clip"/></svg></div><p class="service-name">Maintenance Execution</p></div>
  <div class="service" style="left:43px;top:626px"><div class="service-disc"><svg><use href="#i-tree"/></svg></div><p class="service-name">SCADA</p></div>
  <div class="service" style="left:235px;top:626px"><div class="service-disc"><svg><use href="#i-list"/></svg></div><p class="service-name">Vision Inspection Systems</p></div>
  <div class="service" style="left:428px;top:626px"><div class="service-disc"><svg><use href="#i-hands"/></svg></div><p class="service-name">Acquisition Due Diligence</p></div>

  <div class="welcome-photo" role="img" aria-label="Engineer in hard hat and safety vest using a tablet"></div>
  <p class="eyebrow abs" style="left:345px;top:790px">WELCOME TO</p>
  <h2 class="welcome-title abs" style="left:345px;top:803px">CARLOW &amp; ASSOCIATES</h2>
  <div class="abs" style="left:345px;top:845px;width:230px">
    <p class="copy">Carlow &amp; Associates is specialised manufacturing engineering support organisation that can provide fast, nimble, and flexible services.</p>
    <p class="copy" style="margin-top:13px">We have a proven track record in delivering tangible outcomes in process design and fit-out, project management, manufacturing process and maintenance design and execution.</p>
    <p class="copy" style="margin-top:13px">Our specialist focus in food manufacturing across a range of sectors allows our team to deliver real benefits to performance and recognition of the clients investment</p>
  </div>
  <div class="btn" style="left:345px;top:1024px;width:53px;height:16px">READ MORE</div>

  <div class="stats"></div>
  <div class="band-mist" style="top:1078px;height:293px;clip-path:polygon(0 0,100% 0,100% 250px,328px 293px,0 250px)"></div>
  <div class="why-photo" role="img" aria-label="Engineer in hard hat with city and crane at sunset"></div>
  <svg class="rule" style="left:0;top:1320px" width="649" height="60"><path d="M0 8L328 51" stroke="#5d5d62" stroke-width="4"/><path d="M328 51L649 8" stroke="#6d98cd" stroke-width="4"/></svg>
  <h2 class="section-title section-title--left" style="top:1104px">WHY CHOOSE US</h2>
  <div class="why-item" style="top:1145px"><svg><use href="#i-headset"/></svg><div><p class="why-head">Support</p><p class="why-copy">There are many variations of passages of Lorem Ipsum available, but the majority have.</p></div></div>
  <div class="why-sep" style="top:1197px"></div>
  <div class="why-item" style="top:1210px"><svg><use href="#i-timer"/></svg><div><p class="why-head">Track Record</p><p class="why-copy">There are many variations of passages of Lorem Ipsum available, but the majority have.</p></div></div>
  <div class="why-sep" style="top:1261px"></div>
  <div class="why-item" style="top:1274px"><svg><use href="#i-sun"/></svg><div><p class="why-head">Flexible</p><p class="why-copy">There are many variations of passages of Lorem Ipsum available, but the majority have.</p></div></div>

  <div class="stat-divider" style="left:177px;top:1430px;height:105px"></div>
  <div class="stat-divider" style="left:310px;top:1430px;height:105px"></div>
  <div class="stat" style="left:38px;top:1453px"><svg><use href="#i-case"/></svg><p class="stat-num">10+</p><p class="stat-label">YEARS OF OPERATION</p></div>
  <div class="stat" style="left:167px;top:1453px"><svg><use href="#i-board"/></svg><p class="stat-num">400</p><p class="stat-label">SUCCESSFUL PROJECTS</p></div>
  <div class="stat" style="left:314px;top:1453px"><svg><use href="#i-team"/></svg><p class="stat-num">150</p><p class="stat-label">QUALIFIED PROFESSIONALS</p></div>
  <div class="stat" style="left:458px;top:1453px"><svg><use href="#i-thumb"/></svg><p class="stat-num">6579</p><p class="stat-label">SATISFIED CUSTOMERS</p></div>

  <div class="blog-band"></div>
  <h2 class="section-title" style="top:1593px">LATEST BLOG</h2>
  <article class="post" style="left:71px"><div class="post-photo post-photo--site" role="img" aria-label="Engineers reviewing a construction site"></div><div class="post-body"><h3 class="post-title">Lorem Ipsum is simply dummy text of the printing</h3><p class="post-copy">There are many variations of passages of Lorem Ipsum avail able, but the majority have.</p><div class="btn">READ MORE</div></div></article>
  <article class="post" style="left:245px"><div class="post-photo post-photo--plans" role="img" aria-label="Engineers with plans in a warehouse"></div><div class="post-body"><h3 class="post-title">Lorem Ipsum is simply dummy text of the printing</h3><p class="post-copy">There are many variations of passages of Lorem Ipsum avail able, but the majority have.</p><div class="btn">READ MORE</div></div></article>
  <article class="post" style="left:418px"><div class="post-photo post-photo--data" role="img" aria-label="Tablet showing data charts on a desk"></div><div class="post-body"><h3 class="post-title">Lorem Ipsum is simply dummy text of the printing</h3><p class="post-copy">There are many variations of passages of Lorem Ipsum avail able, but the majority have.</p><div class="btn">READ MORE</div></div></article>

  <div class="band-mist" style="top:1915px;height:260px"></div>
  <div class="feature-photo" role="img" aria-label="Team meeting around a table seen from above"></div>
  <h2 class="feature-title abs" style="left:385px;top:1963px;width:200px">THERE ARE MANY VARIATIONS OF PASSAGES OF LOREM IPSUM AVAILABLE</h2>
  <p class="copy abs" style="left:385px;top:2022px;width:195px;line-height:12.5px">Sed ut perspiciatis unde omnis iste natus error sit voluptatem accusantium doloremque laud antium, totam rem aperiam, eaque ipsa quae ab illo inventore veritatis et quasi architecto beatae vitae dicta sunt explicabo.</p>
  <div class="btn" style="left:386px;top:2101px;width:64px;height:20px">CONTACT US</div>

  <div class="footer"></div>
  <svg class="rule" style="left:0;top:2160px" width="649" height="50"><path d="M0 4L325 46" stroke="#5d5d62" stroke-width="4"/><path d="M325 46L649 4" stroke="#6d98cd" stroke-width="4"/></svg>
  <div class="foot-brand"><span class="brand-mark"></span><span class="brand-name">VILTROP<br>ENGINEERING</span></div>
  <p class="foot-head" style="left:270px">MENU</p>
  <ul class="foot-menu"><li>HOME</li><li>ABOUT US</li><li>SERVICES</li><li>PROJECTS</li><li>NEWS</li><li>CONTACT US</li></ul>
  <p class="foot-head" style="left:374px">CONTACT US</p>
  <div class="foot-row" style="left:374px;top:2258px"><span class="foot-disc"><svg><use href="#i-pin"/></svg></span><p class="foot-text">2210 Harbor Lane<br>Corvale, CA 90410</p></div>
  <div class="foot-row" style="left:374px;top:2285px"><span class="foot-disc"><svg><use href="#i-phone-dark"/></svg></span><p class="foot-text">Call Us<br>888.888.8888</p></div>
  <div class="foot-row" style="left:374px;top:2312px"><span class="foot-disc"><svg><use href="#i-mail-dark"/></svg></span><p class="foot-text">E mail Us<br>info@CarlowAssoc.com</p></div>
  <p class="foot-head" style="left:518px">FOLLOW US</p>
  <div class="foot-row" style="left:518px;top:2258px"><span class="foot-disc"></span><p class="foot-text">Like us on<br>SOCIAL PAGE</p></div>
  <div class="foot-row" style="left:518px;top:2285px"><span class="foot-disc"></span><p class="foot-text">Follow us on<br>NEWS FEED</p></div>
  <div class="foot-row" style="left:518px;top:2312px"><span class="foot-disc"></span><p class="foot-text">Follow us on<br>PRO NETWORK</p></div>
  <div class="foot-line"></div>
  <p class="copyright">Copyright © 2021 All Rights Reserved</p>
</section>

</main>
</body>
</html>
```